Harrow's Electrical & Solar - Business Cards

I want my business card to stand out from the rest. I will provide my business name logo and my icon logo to be implemented onto the card.

On the front of the card, can i have the following. Just make it neat & professional please.

Liam Corbett
harrowselectrical@quillmail.test
0438 917 605
ABN: 41 602 719 384
License No. 582164K
FREE QUOTES
24/7 Emergency

On the back of the card, can I have "Our Services" and maybe add the S logo on the back in the background or something. Under "Our Services" I want the following:

LED Lighting Upgrades
Switches & Outlets
Smoke Alarms
Switchboard Upgrades
Fault Finding
Rewiring
New Builds
Test & Tagging
All Electrical Maintenance & Repairs

Can you guys add the instagram logo and next to it, put harrows_electrical

Can you guys also add the facebook logo and next to it put Harrow's Electrical & Solar. Make sure the instagram & facebook icon is in either white, green or black.

Also I have put down double sided, not sure why when i save it, it keeps going to single sided. I need my business card double sided.

Target Market(s)

New Customers

Contact Information for Business Card

Liam Corbett harrowselectrical@quillmail.test 0438 917 605 ABN: 41 602 719 384 License No. 582164K FREE QUOTES 24/7 Emergency

Requirements
Must have
• must be tidy, professional and appealing

```html
<!DOCTYPE html>
<html lang="en">
<head>
<meta charset="utf-8">
<title>Harrow's Electrical &amp; Solar – Business Cards</title>
<link href="https://fonts.googleapis.com/css2?family=Montserrat:wght@400;500;600;700;800&display=swap" rel="stylesheet">
<style>
  :root {
    --stage: #2c2725;
    --card: #121212;
    --green: #2fb54a;
    --green-bright: #3cc453;
    --white: #f2f2f2;
    --muted: #d9d9d9;
  }
  * { box-sizing: border-box; margin: 0; padding: 0; }
  html, body {
    width: 1200px; height: 716px; overflow: hidden;
    background: var(--stage);
    font-family: 'Montserrat', sans-serif;
  }
  .card {
    position: absolute; top: 193px;
    width: 545px; height: 330px;
    background: var(--card);
    overflow: hidden;
    box-shadow: 0 10px 28px rgba(0,0,0,.45);
  }
  .card--front { left: 45px; }
  .card--back  { left: 610px; }

  .ring {
    position: absolute;
    width: 300px; height: 300px;
    border: 11px solid var(--green);
    border-radius: 50%;
    top: 22px;
  }
  .card--front .ring { left: 405px; }
  .card--back  .ring { left: -160px; }

  /* front */
  .brand-name {
    position: absolute; left: 38px; top: 32px;
    font-size: 25px; font-weight: 800; color: var(--green);
    letter-spacing: .3px;
  }
  .brand-name .dot {
    display: inline-block; width: 12px; height: 12px;
    border-radius: 50%; background: var(--green);
    margin-right: 9px; vertical-align: 2px;
  }
  .contact {
    position: absolute; left: 38px; top: 88px;
    color: var(--white);
  }
  .contact__name {
    font-size: 20px; font-weight: 700; color: var(--green);
    text-transform: uppercase; margin-bottom: 10px;
  }
  .contact__line {
    display: flex; align-items: center; gap: 8px;
    font-size: 14px; font-weight: 500; line-height: 22px;
  }
  .contact__line svg { width: 13px; height: 13px; fill: var(--green); flex: none; }
  .contact__rule {
    width: 52px; height: 2px; background: var(--green);
    margin: 14px 0 12px;
  }
  .contact__meta { font-size: 14px; font-weight: 500; line-height: 22px; }
  .contact__offers {
    margin-top: 12px; font-size: 15px; font-weight: 600;
    text-transform: uppercase; line-height: 22px;
  }
  .contact__offers .accent { color: var(--green); }

  /* back */
  .services {
    position: absolute; right: 30px; top: 38px;
    text-align: right; color: var(--white);
  }
  .services__title {
    font-size: 22px; font-weight: 800; color: var(--green);
    text-transform: uppercase; margin-bottom: 10px; letter-spacing: .3px;
  }
  .services__list { list-style: none; }
  .services__item {
    font-size: 15px; font-weight: 500; line-height: 24px;
    display: flex; justify-content: flex-end; align-items: center; gap: 10px;
  }
  .services__item::after {
    content: ""; width: 7px; height: 7px; border-radius: 50%;
    background: var(--green-bright); flex: none;
  }
</style>
</head>
<body>

  <section class="card card--front" aria-label="Front of card">
    <div class="ring" aria-hidden="true"></div>
    <div class="brand-name"><span class="dot"></span>Harrow's Electrical &amp; Solar</div>
    <div class="contact">
      <div class="contact__name">Liam Corbett</div>
      <div class="contact__line">
        <svg viewBox="0 0 24 24" aria-hidden="true"><path d="M6.6 10.8a15.1 15.1 0 0 0 6.6 6.6l2.2-2.2a1 1 0 0 1 1-.25 11.4 11.4 0 0 0 3.6.57 1 1 0 0 1 1 1V20a1 1 0 0 1-1 1A17 17 0 0 1 3 4a1 1 0 0 1 1-1h3.5a1 1 0 0 1 1 1c0 1.25.2 2.45.57 3.57a1 1 0 0 1-.25 1z"/></svg>
        0438 917 605
      </div>
      <div class="contact__line">
        <svg viewBox="0 0 24 24" aria-hidden="true"><path d="M2 5h20v14H2z M2 5l10 8 10-8" fill="none" stroke="#2fb54a" stroke-width="2.4"/></svg>
        harrowselectrical@quillmail.test
      </div>
      <div class="contact__rule"></div>
      <div class="contact__meta">ABN: 41 602 719 384</div>
      <div class="contact__meta">License No. 582164K</div>
      <div class="contact__offers">
        <div><span class="accent">Free</span> Quotes</div>
        <div><span class="accent">24/7</span> Emergency</div>
      </div>
    </div>
  </section>

  <section class="card card--back" aria-label="Back of card">
    <div class="ring" aria-hidden="true"></div>
    <div class="services">
      <h2 class="services__title">Our Services</h2>
      <ul class="services__list">
        <li class="services__item">LED Lighting Upgrades</li>
        <li class="services__item">Switches &amp; Outlets</li>
        <li class="services__item">Smoke Alarms</li>
        <li class="services__item">Switchboard Upgrades</li>
        <li class="services__item">Fault Finding</li>
        <li class="services__item">Rewiring</li>
        <li class="services__item">New Builds</li>
        <li class="services__item">Test &amp; Tagging</li>
        <li class="services__item">All Electrical Maintenance &amp; Repairs</li>
      </ul>
    </div>
  </section>

</body>
</html>
```